New letterhead design for legal, public interest law firm

THIS IS FOR A LETTERHEAD DESIGN CONTEST , PLEASE REFRAIN FROM SUBMITTING JUST LOGO PROPOSALS AND BUSINESS CARD. LOGO AND BUSINESS CARD PROJECTS WILL BE AWARDED TO THE WINNER OF THE LETTERHEAD DESIGN.
Looking for a timeless, elegant and modern design for our letterhead and logo. Our website is www.hlrbvwn.org so you can incorporate the mission, vision and values into the design. As we also included a request for a NEW LOGO design, please be sure to include logo design options.
We are a public interest criminal defense organization that represents indigent people charged with federal crimes. Please weave the mission/vision/values and our practice area into the logo design.
Target Market(s)
Judges, clients, attorneys, family members of our clients.
Industry/Entity Type
Legal
Contact Information for Business Card
Include line for address, direct line, fax, email address, website address. Remember to incorporate NEW LOGO design.
Logo Text
Harbor Legal Advocates Northern Bureau of Westmoor
Requirements
Must have
- Please remember this project is also to design us a NEW LOGO. Please do not incorporate the existing logo into the new letterhead design.
Nice to have
- Nice to see some logo samples incorporating symbolism for justice, California specific imagery.
Should not have
- New logo should NOT have any traditional/typical legal related images (e.g., scales of justice, etc.)

```html
<!DOCTYPE html>
<html lang="en">
<head>
<meta charset="utf-8">
<title>Harbor Legal Advocates — Letterhead</title>
<link href="https://fonts.googleapis.com/css2?family=Open+Sans:wght@400;600;700&display=swap" rel="stylesheet">
<style>
  :root {
    --brand-blue: #0b55a3;
    --brand-orange: #f28c1e;
    --ink: #4a4a4a;
    --ink-dark: #3a3a3a;
    --page: #ffffff;
    --backdrop: #e6eff9;
  }
  * { box-sizing: border-box; margin: 0; padding: 0; }
  html, body { width: 1200px; height: 1200px; overflow: hidden; }
  body {
    background: var(--backdrop);
    font-family: "Open Sans", sans-serif;
    color: var(--ink);
    position: relative;
  }
  .letterhead {
    position: absolute;
    left: 230px; top: 18px;
    width: 740px; height: 1164px;
    background: var(--page);
    overflow: hidden;
  }
  .brand {
    position: absolute; left: 83px; top: 31px;
    display: flex; align-items: center; gap: 10px;
  }
  .brand-square {
    width: 52px; height: 52px; background: var(--brand-blue); flex: none;
  }
  .brand-name {
    font-weight: 700; color: var(--brand-blue);
    font-size: 15px; line-height: 18px; width: 200px;
  }
  .contacts {
    position: absolute; left: 439px; top: 32px;
    list-style: none; font-size: 12.5px; color: var(--ink);
  }
  .contacts li { display: flex; align-items: center; gap: 9px; height: 20px; white-space: nowrap; }
  .contacts svg { width: 15px; height: 15px; flex: none; }
  .contacts .web-accent { color: var(--brand-blue); }
  .header-rule {
    position: absolute; left: 83px; top: 112px; width: 581px; height: 3px;
    background: var(--brand-blue);
  }
  .recipient { position: absolute; left: 83px; top: 180px; font-size: 14px; }
  .recipient-name { font-weight: 600; color: var(--ink-dark); margin-bottom: 4px; }
  .recipient-line { line-height: 22px; }
  .recipient-line b { color: var(--brand-blue); font-weight: 700; display: inline-block; width: 26px; }
  .letter-date {
    position: absolute; right: 76px; top: 274px; font-size: 12px;
  }
  .salutation {
    position: absolute; left: 83px; top: 292px; font-size: 14px; font-weight: 600; color: var(--ink-dark);
  }
  .letter-body {
    position: absolute; left: 83px; top: 354px; width: 581px;
    font-size: 14.6px; line-height: 22.3px; text-align: justify; hyphens: auto;
  }
  .letter-body p + p { margin-top: 22px; }
  .signature-mark {
    position: absolute; left: 68px; top: 832px; width: 205px; height: 52px;
    background: linear-gradient(90deg, #f1f1f1, #e3e3e3 50%, #f1f1f1);
    border-radius: 4px;
  }
  .signer { position: absolute; left: 84px; top: 898px; font-size: 14px; line-height: 22px; }
  .signer-name { font-weight: 700; color: var(--ink); }
  .footer-band {
    position: absolute; left: 0; top: 1030px; width: 740px; height: 134px;
    background: linear-gradient(90deg, rgba(11,85,163,0.22) 0%, rgba(11,85,163,0.16) 55%, rgba(242,140,30,0.2) 100%);
  }
</style>
</head>
<body>
  <main class="letterhead">
    <div class="brand">
      <span class="brand-square"></span>
      <span class="brand-name">Harbor Legal Advocates Northern Bureau of Westmoor</span>
    </div>

    <ul class="contacts">
      <li><svg viewBox="0 0 16 16"><rect width="16" height="16" rx="2" fill="#0b55a3"/><path d="M8 3a3.2 3.2 0 0 0-3.2 3.2C4.8 9 8 13 8 13s3.2-4 3.2-6.8A3.2 3.2 0 0 0 8 3z" fill="#fff"/><circle cx="8" cy="6.2" r="1.2" fill="#0b55a3"/></svg><span>17/B, Gullwing Lane, Westmoor</span></li>
      <li><svg viewBox="0 0 16 16"><rect width="16" height="16" rx="2" fill="#0b55a3"/><path d="M4.5 3.5l2 .2.8 2.3-1.2 1a6 6 0 0 0 2.9 2.9l1-1.2 2.3.8.2 2c-4.5.6-8.6-3.5-8-8z" fill="#fff"/></svg><span>+1 555 014 2290</span></li>
      <li><svg viewBox="0 0 16 16"><rect x=".5" y="2.5" width="15" height="11" fill="#fff" stroke="#0b55a3"/><path d="M1 3l7 6 7-6M1 13l5-5M15 13l-5-5" fill="none" stroke="#0b55a3"/></svg><span>contact@hlrbvwn.org</span></li>
      <li><svg viewBox="0 0 16 16"><rect width="16" height="16" rx="2" fill="#0b55a3"/><circle cx="8" cy="8" r="5" fill="none" stroke="#fff"/><path d="M3 8h10M8 3v10M8 3c-2.5 2.5-2.5 7.5 0 10M8 3c2.5 2.5 2.5 7.5 0 10" fill="none" stroke="#fff" stroke-width=".8"/></svg><span>www.<span class="web-accent">hlrbvwn</span>.org</span></li>
    </ul>

    <div class="header-rule"></div>

    <section class="recipient">
      <p class="recipient-name">NORVELLE PARTNERS, LLC</p>
      <p class="recipient-line"><b>A :</b>28-4, Corran Avenue Westmoor - 4471</p>
      <p class="recipient-line"><b>W:</b>www.norvellepartners.com</p>
      <p class="recipient-line"><b>P :</b>+1 - 55501 - 3342</p>
    </section>

    <p class="letter-date">Date, 10 September, 2020</p>
    <p class="salutation">Dear, Marlow</p>

    <article class="letter-body">
      <p>Contrary to popular belief, Lorem Ipsum is not simply random text. It has roots in a piece of classical Latin literature from 45 BC, making it over 2000 years old. Arden Voss, a Latin professor at Kestrel Hill College in Westmoor, looked up one of the more obscure Latin words, consectetur, from a Lorem Ipsum passage, and going through the cites of the word in classical literature, discovered the undoubtable source.</p>
      <p>Lorem Ipsum comes from sections 1.10.32 and 1.10.33 of "de Finibus Bonorum et Malorum" (The Extremes of Good and Evil) by Corvinus, written in 45 BC. This book is a treatise on the theory of ethics, very popular during the Renaissance. Lorem Ipsum used since the 1500s is reproduced below for those interested. Sections 1.10.32 and 1.10.33 from "de Finibus Bonorum et Malorum" by Corvinus are also reproduced in their exact original form, accompanied by English versions from the 1914 translation by T. Wexley.</p>
      <p>Contrary to popular belief, Lorem Ipsum is not simply random text. It has roots in a piece of classical Latin literature from 45 BC, making it over 2000 years old. Arden Voss, a Latin professor at Kestrel Hill College in Westmoor, looked up one of the more obscure Latin words.</p>
    </article>

    <div class="signature-mark" role="img" aria-label="Handwritten signature of Elena R. Castellan"></div>
    <div class="signer">
      <p class="signer-name">Elena R. Castellan</p>
      <p>General Director</p>
    </div>

    <div class="footer-band" role="img" aria-label="Decorative footer pattern in brand blue and orange"></div>
  </main>
</body>
</html>
```